Flyer Design for Southern Guild of Mindful Listeners and Carers (SGMLC)

We need a new flyer designed for SGMLC. We want to attract new members @ a tradeshow. Counsellors and Psychotherapists looking for a professional association with which to align themselves where they feel @ home because they share similar values.We would like to use the colours and leaves from our website which is www.sgmlc-guild.org if possible or similar colours and the photo of the tree in bloom from Facebook "stillwaterandcarework". As well as our logo (www.sgmlc-guild.org), the TOVRE (www.tovre-hub.org) logo as well somewhere in the bottom corner the Quiet Path Forum logo (www.quietpathforum.org).

Target Market(s)

Psychotherapists and Counsellors

Industry/Entity Type

Mental Health

Colors
876aae
b7a5cd
e4daeb
cadf82
abd036
9bcb3b

Requirements
Must have
• Logo
Nice to have
• Warm inviting photo of lotus flower
Should not have
• No monks

```html
<!DOCTYPE html>
<html lang="en">
<head>
<meta charset="utf-8">
<title>SGMLC Flyer</title>
<link href="https://fonts.googleapis.com/css2?family=Arimo:wght@400;700&display=swap" rel="stylesheet">
<style>
  :root {
    --lavender-deep: #876aae;
    --lavender-mid: #b7a5cd;
    --lavender-pale: #e4daeb;
    --lavender-bg: #ece6f2;
    --tab-grey: #5b5b5d;
    --text-grey: #6a6a6a;
    --ink: #2b2b2b;
    --white: #ffffff;
    --footer-grey: #d9d9db;
  }
  * { box-sizing: border-box; margin: 0; padding: 0; }
  html, body { width: 900px; height: 1200px; overflow: hidden; background: var(--lavender-bg); }
  body { font-family: "Arimo", Arial, sans-serif; }
  .flyer { position: relative; width: 900px; height: 1200px; overflow: hidden; background: var(--lavender-bg); }

  .hero { position: absolute; left: 0; top: 0; width: 900px; height: 560px; }

  .brand-card {
    position: absolute; left: 30px; top: 22px; width: 278px; height: 190px;
    background: var(--lavender-pale); border-radius: 22px;
    display: flex; flex-direction: column; align-items: center; justify-content: center; gap: 18px;
    box-shadow: 0 3px 8px rgba(0,0,0,.25);
  }
  .brand-name { font-size: 44px; font-weight: 400; color: var(--ink); letter-spacing: 2px; }
  .brand-dot { width: 70px; height: 70px; border-radius: 50%; background: var(--ink); }

  .side-photo {
    position: absolute; left: 14px; width: 266px; border-radius: 18px;
    border: 6px solid var(--lavender-mid);
    box-shadow: 0 2px 6px rgba(0,0,0,.2);
  }
  .side-photo--butterfly { top: 526px; height: 190px; background: linear-gradient(135deg, #2fb8b0 0%, #54c9bf 55%, #a6e3da 100%); }
  .side-photo--blossom { top: 738px; height: 188px; background: linear-gradient(120deg, #f3eef2 0%, #dcd2da 45%, #3a3636 100%); }
  .side-photo--droplets { top: 940px; height: 192px; background: linear-gradient(160deg, #9fdcd8 0%, #45b9b6 50%, #1f8f94 100%); }

  .panel { position: absolute; left: 338px; width: 520px; border-radius: 0 0 26px 0; }
  .panel--vision {
    top: 500px; height: 210px;
    background: linear-gradient(90deg, #ffffff 0%, #ececec 60%, #c9c9cb 100%);
    box-shadow: 0 4px 8px rgba(0,0,0,.2);
    padding: 60px 18px 0 20px;
  }
  .panel--goals {
    top: 730px; height: 408px; border-radius: 26px;
    background: linear-gradient(90deg, #ded3ea 0%, #b7a5cd 55%, #9a82bf 100%);
    box-shadow: 0 4px 8px rgba(0,0,0,.2);
    padding: 70px 24px 0 30px;
  }
  .panel-tab {
    position: absolute; left: -14px; height: 34px; padding: 0 46px 0 30px;
    background: linear-gradient(180deg, #6e6e70, var(--tab-grey));
    color: var(--white); font-weight: 700; font-size: 25px; line-height: 34px;
    clip-path: polygon(0 0, 92% 0, 100% 100%, 0 100%);
    border-radius: 4px 0 0 4px;
  }
  .panel--vision .panel-tab { top: 20px; }
  .panel--goals .panel-tab { top: 20px; }

  .vision-text { font-size: 12.8px; line-height: 1.25; color: var(--text-grey); margin-bottom: 12px; hyphens: auto; }

  .goal-list { list-style: none; color: var(--white); font-size: 18px; line-height: 1.3; }
  .goal-list li { position: relative; padding-left: 22px; margin-bottom: 3px; }
  .goal-list li::before { content: "•"; position: absolute; left: 2px; top: 0; }

  .footer-bar {
    position: absolute; left: 78px; top: 1152px; width: 724px; height: 48px;
    background: linear-gradient(180deg, #e6e6e8, var(--footer-grey));
    border-radius: 24px 24px 0 0;
    text-align: center; line-height: 48px;
    font-size: 27px; font-weight: 700; color: var(--lavender-deep); letter-spacing: 9px;
  }
</style>
</head>
<body>
<main class="flyer">
  <svg class="hero" viewBox="0 0 900 560" xmlns="http://www.w3.org/2000/svg">
    <defs>
      <linearGradient id="sunsetTones" x1="0" y1="0" x2="0" y2="1">
        <stop offset="0" stop-color="#c7c4bd"/>
        <stop offset="0.3" stop-color="#e9cfa6"/>
        <stop offset="0.55" stop-color="#b8a487"/>
        <stop offset="1" stop-color="#4a4638"/>
      </linearGradient>
      <linearGradient id="waveBand" x1="0" y1="0" x2="1" y2="0">
        <stop offset="0" stop-color="#b7a5cd"/>
        <stop offset="1" stop-color="#9d86c0"/>
      </linearGradient>
    </defs>
    <rect width="900" height="560" fill="url(#sunsetTones)" role="img" aria-label="Photo: mountain landscape at sunset with a calm seated figure looking out over the hills"/>
    <path d="M0,498 C250,430 560,520 900,250 L900,560 L0,560 Z" fill="url(#waveBand)"/>
    <path d="M0,532 C280,468 600,540 900,330 L900,560 L0,560 Z" fill="#f6f2f9"/>
    <path d="M0,544 C300,490 620,560 900,362 L900,560 L0,560 Z" fill="#ece6f2"/>
  </svg>

  <div class="brand-card">
    <span class="brand-name">SGMLC</span>
    <span class="brand-dot"></span>
  </div>

  <div class="side-photo side-photo--butterfly" role="img" aria-label="Photo: orange butterfly on white flowers against a teal sky"></div>
  <div class="side-photo side-photo--blossom" role="img" aria-label="Photo: close-up of pale pink blossoms on a dark background"></div>
  <div class="side-photo side-photo--droplets" role="img" aria-label="Photo: water droplets resting on a teal leaf"></div>

  <section class="panel panel--vision">
    <h2 class="panel-tab">Our Vision</h2>
    <p class="vision-text">The purpose of The Southern Guild of Mindful Listeners and Carers (SGMLC), a TOVRE Member Association, is to bring the whole philosophy and practice of Buddhism (the dhamma), to therapists and counsellors, using innovative educational experiences.</p>
    <p class="vision-text">The benefits of introducing Buddhist practices into mental health is now scientifically validated, as increasing the effectiveness of Western psychotherapeutic approaches, as well as taking care of therapists in particular ‘burnout’.</p>
  </section>

  <section class="panel panel--goals">
    <h2 class="panel-tab">Our Goals</h2>
    <ul class="goal-list">
      <li>To present Buddhism in a thorough way</li>
      <li>To explore and discuss dhamma and how it can improve the effectiveness of a therapist’s life</li>
      <li>To provide ongoing education in all aspects of Buddhism for mental health professionals</li>
      <li>To develop a dynamic organisation that stays attuned to changes in Buddhism as it is expressed in the West</li>
      <li>To develop a strong membership/community</li>
      <li>To develop a relevant and important voice in the community</li>
      <li>To develop a unique professional identity</li>
      <li>To encourage positive social change</li>
    </ul>
  </section>

  <footer class="footer-bar">www.sgmlc-guild.org</footer>
</main>
</body>
</html>
```